Torvik-Ellingsen Global AS

We need a design for our company including background pictures on our web (wix-template), redesign of logo and reports. Our company delivers personality test and services to clients when hiring staff or related to organizatonal developement.

Target Market(s)

Unisex, Age 30-50, managers in private corporations

Industry/Entity Type

Recruitment

Logo Text

Bygger laget sterkt (english translate: buids your team strong)

Number of Pages Required

1 page

Font styles to use
Sans Serif

Colors
add136
34a6d7
0255a3

Requirements
Must have
• The ideal designer will be the one to bring my narrative come to life. And it will have to include the testresults report and redesign (!) of my logo. Following the attached brief in ppt:
• - the testresult report
• - redesign logo
• - graphic elements in a maritime narrative
• - including the boat, the radar, 4 WINDs, the compass etc
Nice to have
• A strong narrative with a lot of elements.
• I really like the green color in the attached breif ;-)

```html
<!DOCTYPE html>
<html lang="no">
<head>
<meta charset="utf-8">
<title>Torvik-Ellingsen Global AS – Testresultat</title>
<link href="https://fonts.googleapis.com/css2?family=Lato:wght@400;700&display=swap" rel="stylesheet">
<style>
  :root {
    --black: #000000;
    --brand-green: #4a6a1f;
    --orange: #f58220;
    --sky: #34a6d7;
    --lime: #7ab52f;
    --navy: #0255a3;
    --deep-navy: #1c3d6b;
    --bar-blue: #1f8fcf;
    --bar-red: #f24a1c;
    --label-blue: #1a73c9;
    --text: #333333;
    --muted: #777777;
    --field-bg: #f0f0f0;
    --field-border: #c9c9c9;
    --footer-bg: #dcdcdc;
  }
  * { box-sizing: border-box; margin: 0; padding: 0; }
  html, body { width: 889px; height: 1200px; overflow: hidden; background: #fff; }
  body { position: relative; font-family: "Lato", sans-serif; color: var(--text); }

  .site-header { position: absolute; left: 0; top: 0; width: 889px; height: 96px; background: var(--black); }
  .site-header .brand { position: absolute; left: 122px; top: 36px; color: var(--brand-green); font-weight: 700; font-size: 20px; }

  .journey { position: absolute; left: 0; top: 96px; width: 889px; height: 281px;
    background: radial-gradient(ellipse at 85% 20%, #d9d9d9 0%, #f0f0f0 45%, #f7f7f7 100%); }
  .journey svg { position: absolute; left: 0; top: 0; }
  .stage-label { position: absolute; font-weight: 700; font-size: 14px; color: #111; transform: translateX(-50%); }

  .report-card { position: absolute; left: 125px; top: 399px; width: 479px; height: 725px; background: #fff;
    box-shadow: 0 0 4px rgba(0,0,0,0.25); }
  .compass { position: absolute; left: 125px; top: 20px; width: 224px; height: 224px; border-radius: 50%;
    background: radial-gradient(circle, #ffffff 0%, #e3e9f1 55%, #1c3d6b 57%, #ffffff 60%, #dfe6ef 95%, #1c3d6b 97%); }

  .metric-label { position: absolute; font-size: 14px; color: var(--text); }
  .battery { position: absolute; width: 156px; height: 35px; border: 2px solid #cfcfcf; padding: 3px; display: flex; }
  .battery::after { content: ""; position: absolute; right: -7px; top: 9px; width: 5px; height: 13px; border: 2px solid #cfcfcf; border-left: none; }
  .fill-blue { background: repeating-linear-gradient(135deg, var(--bar-blue) 0 3px, #2a9ad8 3px 5px); }
  .fill-red { background: repeating-linear-gradient(135deg, var(--bar-red) 0 3px, #ff5a2a 3px 5px); }

  .bar-label { position: absolute; font-size: 8px; color: var(--text); }
  .level-bar { position: absolute; width: 55px; height: 97px; background: #d6d6d6; padding: 4px; display: flex; flex-direction: column; }
  .scale-mark { position: absolute; left: 223px; font-size: 11px; color: #555; }

  .field-label { position: absolute; width: 90px; text-align: right; font-size: 12px; color: var(--label-blue); }
  .field { position: absolute; left: 105px; width: 327px; background: linear-gradient(#fafafa, var(--field-bg)); border: 1px solid var(--field-border);
    font-size: 11px; color: #555; padding: 8px 12px; }
  .field.profile { font-size: 7.5px; line-height: 13.5px; padding: 12px 16px; color: #777; }

  .site-footer { position: absolute; left: 0; top: 1146px; width: 889px; height: 54px; background: var(--footer-bg); }
  .site-footer .legal { position: absolute; right: 81px; top: 21px; font-size: 9px; color: #444; }
  .site-footer .page-code { position: absolute; right: 9px; top: 31px; font-size: 8px; color: #444; }
</style>
</head>
<body>
  <header class="site-header">
    <span class="brand">Torvik-Ellingsen Global AS</span>
  </header>

  <section class="journey" aria-label="Profilreisen">
    <svg width="889" height="281" viewBox="0 0 889 281">
      <path d="M170 218 C210 200 240 170 281 138 C320 90 360 55 400 60 C440 70 470 120 438 138 M438 80 C470 40 540 40 590 66 M620 70 C660 78 690 82 712 78"
            fill="none" stroke="#999" stroke-width="2.5" stroke-dasharray="1 5" stroke-linecap="round"/>
      <circle cx="438" cy="138" r="58" fill="none" stroke="#999" stroke-width="2.5" stroke-dasharray="1 5" stroke-linecap="round"/>
      <circle cx="438" cy="138" r="44" fill="var(--brand-green)"/>
      <g stroke="#bbb" stroke-width="2">
        <circle cx="154" cy="230" r="31" fill="var(--orange)"/>
        <circle cx="281" cy="138" r="31" fill="var(--sky)"/>
        <circle cx="590" cy="66" r="31" fill="var(--lime)"/>
        <circle cx="743" cy="62" r="31" fill="var(--navy)"/>
      </g>
      <g fill="none" stroke="#fff" stroke-width="2.5" stroke-linecap="round">
        <line x1="154" y1="218" x2="154" y2="232"/><circle cx="154" cy="240" r="1.5" fill="#fff"/>
        <path d="M271 140 l8 8 l12 -16"/>
        <circle cx="590" cy="66" r="9"/><line x1="590" y1="60" x2="590" y2="72"/><line x1="584" y1="66" x2="596" y2="66"/>
        <line x1="737" y1="54" x2="737" y2="70"/><line x1="743" y1="54" x2="743" y2="70"/><line x1="749" y1="54" x2="749" y2="70"/>
      </g>
    </svg>
    <span class="stage-label" style="left:152px;top:178px;">Worker</span>
    <span class="stage-label" style="left:274px;top:86px;">Integrator</span>
    <span class="stage-label" style="left:590px;top:106px;">Navigator</span>
    <span class="stage-label" style="left:744px;top:100px;">Dicipline</span>
  </section>

  <main class="report-card">
    <div class="compass" role="img" aria-label="Kompassrose med gradskala og himmelretninger"></div>

    <span class="metric-label" style="left:57px;top:260px;">Energi</span>
    <div class="battery" style="left:57px;top:283px;"><div class="fill-blue" style="flex:1"></div><div class="fill-red" style="flex:1"></div></div>

    <span class="metric-label" style="left:283px;top:260px;">Problemløsningsevne</span>
    <div class="battery" style="left:283px;top:283px;"><div class="fill-blue" style="flex:1"></div><div class="fill-red" style="flex:1"></div></div>

    <span class="metric-label" style="left:57px;top:334px;">Lytte</span>
    <svg style="position:absolute;left:105px;top:328px;" width="30" height="30" viewBox="0 0 30 30" fill="none" stroke="var(--sky)" stroke-width="2">
      <circle cx="15" cy="15" r="13"/><circle cx="15" cy="15" r="8"/><circle cx="15" cy="15" r="3"/>
    </svg>
    <span class="metric-label" style="left:284px;top:335px;">Sende</span>
    <svg style="position:absolute;left:350px;top:332px;" width="30" height="26" viewBox="0 0 30 26" fill="none" stroke="var(--bar-red)" stroke-width="2" stroke-linejoin="round">
      <path d="M3 9 h7 l14 -7 v20 l-14 -7 h-7 z"/><path d="M7 15 l2 8 h4 l-2 -8"/>
    </svg>

    <span class="bar-label" style="left:58px;top:371px;">Empati</span>
    <span class="bar-label" style="left:135px;top:371px;">Profesjonell</span>
    <span class="bar-label" style="left:288px;top:369px;">Overbevisningsevne</span>
    <span class="bar-label" style="left:372px;top:369px;">Autoritet</span>

    <div class="level-bar" style="left:58px;top:385px;"><div class="fill-red" style="flex:26"></div><div class="fill-blue" style="flex:63"></div></div>
    <div class="level-bar" style="left:135px;top:385px;"><div class="fill-red" style="flex:68"></div><div class="fill-blue" style="flex:21"></div></div>
    <div class="level-bar" style="left:285px;top:385px;"><div class="fill-red" style="flex:46"></div><div class="fill-blue" style="flex:43"></div></div>
    <div class="level-bar" style="left:372px;top:385px;"><div class="fill-red" style="flex:68"></div><div class="fill-blue" style="flex:21"></div></div>

    <span class="scale-mark" style="top:390px;">- 1 -</span>
    <span class="scale-mark" style="top:410px;">- 2 -</span>
    <span class="scale-mark" style="top:430px;">- 3 -</span>
    <span class="scale-mark" style="top:450px;">- 4 -</span>
    <span class="scale-mark" style="top:471px;">- 5 -</span>

    <span class="field-label" style="left:0;top:543px;">Name:</span>
    <div class="field" style="top:539px;height:28px;">Erik Solberg</div>
    <span class="field-label" style="left:0;top:583px;">Company:</span>
    <div class="field" style="top:579px;height:28px;">Nordhavn Rådgivning Limited</div>
    <span class="field-label" style="left:0;top:620px;">Profile:</span>
    <div class="field profile" style="top:618px;height:82px;">Morbi diam mauris viverra in gravida eu mattis in ante Morbi eget arcu Morbi porta libero id ullamcorper nonummy nibh ligula pulvinar metus eget consectetuer augue nisi quis lacus Ut ac mi quis lacus mollis aliquam Curabitur iaculis tempus eros Curabitur vel mi sit amet magna malesuad</div>
  </main>

  <footer class="site-footer">
    <span class="legal">© 2017 Company Name &nbsp;All right reserved &nbsp;Terms of Use</span>
    <span class="page-code">X14</span>
  </footer>
</body>
</html>
```